Startup online payment business - Sporting / Golf, Swift Tee payment

Background:
Our business name is "Swift Tee" we provide online payments for golfing services via our website. We currently have a logo used on our website. No other design style has been developed. Our aim is to remove cash payments for service at golf clubs.

Our Key Values:
Quick and easy
Formal and polite
Fun with professional boundary
Mate-ship relationships
100% online digital

What we want from you:
Marketing design to be used on posters and stickers in a retail setting to direct customers to our online payment Chanel.
Design must incorporate attached logo, URL swifttee.com.au and our key values can act as a guide the type of design. We have used color Hex#007672 for logo background. We are open to use other colors.

Target Market(s)

Golf clubs and golf players

Industry/Entity Type

Golf Course

Font styles to use
Sans Serif

Requirements
Must have
• Directions to online payment via URL: swifttee.com.au
Nice to have
• We like the idea of the slogan: No Cash - No worries. Have attached home screen that will be available from URL link. Consideration if using mobile phone in image. Push the online payment and steps 1. Visit swifttee.com 2. Select club 3. Confirm payment
Should not have
• Cartoons

```html
<!DOCTYPE html>
<html lang="en">
<head>
<meta charset="utf-8">
<title>Swift Tee – No Cash? No Worries!</title>
<link rel="stylesheet" href="https://fonts.googleapis.com/css2?family=Bebas+Neue&family=Roboto+Condensed:ital,wght@0,300;0,400;0,700;1,700&display=swap">
<style>
  :root {
    --teal: #007672;
    --teal-deep: #04524f;
    --teal-dark: #023f3d;
    --gold-light: #eef06a;
    --gold-mid: #cfcf3c;
    --gold-dark: #8a8620;
    --gold-label: #c9b92c;
    --white: #ffffff;
    --ink: #2b2b2b;
    --skin: #d9a98a;
  }
  html, body { margin: 0; padding: 0; overflow: hidden; }
  body { width: 958px; height: 1200px; background: var(--teal); }

  .poster {
    position: relative;
    width: 958px;
    height: 1200px;
    overflow: hidden;
    background: var(--teal);
    font-family: "Roboto Condensed", sans-serif;
    color: var(--white);
  }

  .course-photo {
    position: absolute;
    left: 0; top: 540px;
    width: 958px; height: 540px;
    background: linear-gradient(180deg, var(--teal) 0%, var(--teal-deep) 35%, var(--teal-dark) 100%);
  }
  .club-photo {
    position: absolute;
    left: 0; top: 780px;
    width: 380px; height: 230px;
    background: radial-gradient(ellipse at 65% 70%, #1d6a66 0%, rgba(2,63,61,0) 65%);
  }
  .phone-photo {
    position: absolute;
    left: 600px; top: 482px;
    width: 358px; height: 545px;
    border-radius: 40px 0 0 0;
    background:
      linear-gradient(180deg, rgba(0,118,114,0.95) 0%, rgba(0,118,114,0.9) 55%, rgba(46,140,90,0.9) 80%, rgba(217,169,138,0.6) 100%),
      var(--skin);
  }

  .headline {
    position: absolute;
    left: 94px; top: 60px;
    margin: 0;
    font-family: "Bebas Neue", sans-serif;
    font-weight: 400;
    font-size: 168px;
    line-height: 140px;
    letter-spacing: 1px;
    background: linear-gradient(100deg, var(--gold-light) 0%, var(--gold-mid) 45%, var(--gold-dark) 75%, var(--gold-light) 100%);
    -webkit-background-clip: text;
    background-clip: text;
    color: transparent;
  }
  .headline span { display: block; }

  .intro {
    position: absolute;
    left: 97px; top: 340px;
    width: 520px;
    margin: 0;
    font-weight: 300;
    font-size: 21px;
    line-height: 26px;
  }

  .values-title {
    position: absolute;
    left: 97px; top: 484px;
    margin: 0;
    padding: 0 8px;
    height: 30px;
    border: 1px solid var(--gold-label);
    font-family: "Bebas Neue", sans-serif;
    font-weight: 400;
    font-size: 30px;
    line-height: 33px;
    color: var(--gold-label);
  }

  .values {
    position: absolute;
    left: 97px; top: 534px;
    margin: 0; padding: 0;
    list-style: none;
    font-weight: 400;
    font-size: 24px;
    line-height: 26px;
  }
  .values li {
    position: relative;
    padding-left: 32px;
    margin-bottom: 10px;
  }
  .values li svg {
    position: absolute;
    left: 0; top: 2px;
    width: 20px; height: 20px;
  }

  .footer-band {
    position: absolute;
    left: 0; top: 1020px;
    width: 958px; height: 180px;
  }

  .register {
    position: absolute;
    left: 97px; top: 1108px;
  }
  .register-note {
    margin: 0;
    font-weight: 400;
    font-size: 16px;
    color: var(--ink);
  }
  .register-url {
    display: inline-block;
    margin-top: 2px;
    padding: 0 4px;
    background: var(--teal);
    color: var(--white);
    font-weight: 700;
    font-size: 27px;
    line-height: 28px;
    text-decoration: none;
  }

  .tagline {
    position: absolute;
    left: 346px; top: 1128px;
    margin: 0;
    font-style: italic;
    font-weight: 700;
    font-size: 27px;
    color: var(--teal);
  }

  .brand-box {
    position: absolute;
    left: 704px; top: 1058px;
    width: 214px; height: 142px;
    background: var(--teal);
    display: flex;
    align-items: center;
    justify-content: center;
  }
  .brand-name {
    font-family: "Bebas Neue", sans-serif;
    font-weight: 400;
    font-size: 52px;
    letter-spacing: 2px;
    color: var(--white);
  }
</style>
</head>
<body>
<main class="poster">
  <div class="course-photo" role="img" aria-label="Golf turf in teal tones"></div>
  <div class="club-photo" role="img" aria-label="Golf iron resting behind a golf ball on the grass"></div>
  <div class="phone-photo" role="img" aria-label="Hand holding a smartphone showing the Swift Tee welcome screen"></div>

  <h1 class="headline"><span>No Cash?</span><span>No Worries!</span></h1>

  <p class="intro">Moving toward a future cashless society, Swift Tee are developing new mobile payment methods in order for Clubs to cater for the next generation of players and community expectations.</p>

  <h2 class="values-title">Our Key Values</h2>
  <ul class="values">
    <li><svg viewBox="0 0 20 20"><circle cx="10" cy="10" r="10" fill="#0a8a84"/><path d="M5 10.5l3.5 3.5L15 6.5" fill="none" stroke="#d8c430" stroke-width="2.6" stroke-linecap="round" stroke-linejoin="round"/></svg>Quick and easy</li>
    <li><svg viewBox="0 0 20 20"><circle cx="10" cy="10" r="10" fill="#0a8a84"/><path d="M5 10.5l3.5 3.5L15 6.5" fill="none" stroke="#d8c430" stroke-width="2.6" stroke-linecap="round" stroke-linejoin="round"/></svg>Formal and polite</li>
    <li><svg viewBox="0 0 20 20"><circle cx="10" cy="10" r="10" fill="#0a8a84"/><path d="M5 10.5l3.5 3.5L15 6.5" fill="none" stroke="#d8c430" stroke-width="2.6" stroke-linecap="round" stroke-linejoin="round"/></svg>Fun with professional<br>boundary</li>
    <li><svg viewBox="0 0 20 20"><circle cx="10" cy="10" r="10" fill="#0a8a84"/><path d="M5 10.5l3.5 3.5L15 6.5" fill="none" stroke="#d8c430" stroke-width="2.6" stroke-linecap="round" stroke-linejoin="round"/></svg>Mate-ship relationships</li>
    <li><svg viewBox="0 0 20 20"><circle cx="10" cy="10" r="10" fill="#0a8a84"/><path d="M5 10.5l3.5 3.5L15 6.5" fill="none" stroke="#d8c430" stroke-width="2.6" stroke-linecap="round" stroke-linejoin="round"/></svg>100% online digital</li>
  </ul>

  <svg class="footer-band" viewBox="0 0 958 180" aria-hidden="true">
    <polygon points="0,38 720,38 750,7 958,7 958,180 0,180" fill="#ffffff"/>
    <polygon points="730,42 760,7 767,7 737,42" fill="#007672"/>
  </svg>

  <div class="register">
    <p class="register-note">Register here via online payment</p>
    <a class="register-url" href="https://swifttee.com.au">swifttee.com.au</a>
  </div>

  <p class="tagline">Safer and faster way to pay</p>

  <div class="brand-box">
    <span class="brand-name">Swift Tee</span>
  </div>
</main>
</body>
</html>
```